Real Estate Development and Brokerage Middle East

Required is a web site design for a new branch of an existing Real Estate Development and Brokerage company. The Branch will be established in the United Arab Emirates - Veluna Middle East, the mother company is based in Austria/Europe. The new branch focuses on the middle eastern clients such as Institutional Investors/Family Businesses/Wealthy Individuals looking either for a luxury home in Vienna City or the alpine nature or are interested to invest in ready made properties or real estate development projects in Austria run by the branches mother co. in Austria. The design should highlight both Services i.e. Investment for commercial purpose and for residential purposes (focus on the nature) as well as the companies focus on high end luxury selected properties only and having middle east experienced staff in the UAE.

The link to the Austrian HQ website is below: Design elements of that website might or might not be used, however the logo shall be the same.
http://plenodraft.example/QW7RTZMBX

Attached the logo and a rough first draft of the structure of the website (not yet set in stone) . The attachment contains also a link to a website of a company in a similar industry. I do like the way they present the highlights on their start/home page. The boxes. By the way, we believe that more graphic (pictures) and a bit less text might be a good way to approach our future target customers.

As we hope to sell many of the projects and hence many new projects descriptions/pictures will be uploaded in future on an ongoing basis the page should have the ability to upload information and pics by our team (none of it is a web designer and has experience exceeding MS-Office).

Lastly - and for the future we might need (not sure yet) need the entire context in Arabic (the language button)

Thanks.
Lars

Target Market(s)

Institutional Investors and wealthy individuals / family offices

Industry/Entity Type

Real Estate

Coding

Number of Pages Required

5+ page

Requirements
Must have
• Same Logo as Parent Company
Nice to have
• News ticker/banner, high resolution picture heavy, changing pictures on start/home page, PDF downloads

```html
<!DOCTYPE html>
<html lang="en">
<head>
<meta charset="utf-8">
<title>Veluna Real Estate – Middle East</title>
<link href="https://fonts.googleapis.com/css2?family=Open+Sans:ital,wght@0,400;0,600;0,700;1,400&display=swap" rel="stylesheet">
<style>
:root{
  --ink:#333333;
  --muted:#777777;
  --nav:#3b3b3b;
  --nav-active:#5f8fb2;
  --accent:#4f7ea3;
  --accent-dark:#3c6486;
  --red:#d9362b;
  --band-top:#7392ab;
  --band-bottom:#3f5f7a;
  --dark:#2d2d2d;
  --light:#e9eaec;
  --white:#ffffff;
  --date:#d9483b;
  --link:#3f74a8;
}
*{box-sizing:border-box;margin:0;padding:0}
html,body{width:1200px;height:2292px;overflow:hidden}
body{font-family:"Open Sans",Arial,sans-serif;color:var(--ink);background:var(--white);position:relative}
.wrap{width:960px;margin:0 auto;position:relative}

/* header */
.site-header{height:160px;position:relative}
.brand{position:absolute;left:120px;top:34px;display:flex;align-items:center;gap:14px}
.brand-square{width:46px;height:46px;background:var(--accent)}
.brand-name{font-size:34px;font-weight:600;color:var(--ink);letter-spacing:-.5px}
.header-actions{position:absolute;right:140px;top:12px;display:flex;flex-direction:column;align-items:flex-end;gap:10px}
.btn-profile{display:flex;align-items:center;gap:10px;height:28px;padding:0 14px 0 6px;background:var(--white);border:1px solid #d5d5d5;font-size:11px;font-weight:700;color:var(--red)}
.btn-login{height:26px;padding:0 16px;background:var(--accent);color:var(--white);font-size:11px;font-weight:600;line-height:26px}

.main-nav{height:40px;background:var(--nav)}
.main-nav ul{list-style:none;display:flex;width:960px;margin:0 auto;height:40px}
.main-nav li{font-size:13px;font-weight:600;color:#e6e6e6;line-height:40px;padding:0 26px}
.main-nav li.active{background:var(--nav-active);color:var(--white);padding:0 40px}

/* hero */
.hero{height:450px;position:relative;overflow:hidden}
.hero-photo{position:absolute;inset:0;background:linear-gradient(180deg,#a9c3d9 0%,#cfdde8 45%,#7fa0b8 62%,#52778f 100%)}
.hero-building{position:absolute;right:0;top:0;width:620px;height:450px;background:linear-gradient(120deg,#e8edf0 0%,#b8c6cf 40%,#6d8596 100%)}
.hero-copy{position:absolute;left:120px;top:72px;width:520px;color:var(--white)}
.hero-title{font-size:31px;font-weight:600;line-height:44px;letter-spacing:.3px}
.hero-text{margin-top:14px;font-size:13px;line-height:20px;width:420px}
.btn-more{display:inline-block;margin-top:18px;background:#2b2b2b;color:var(--white);font-size:12px;padding:10px 20px}
.hero-dots{position:absolute;left:122px;bottom:14px;display:flex;gap:7px}
.hero-dots span{width:10px;height:10px;border-radius:50%;background:rgba(255,255,255,.55)}
.hero-dots span.on{background:var(--white)}

/* features */
.features{height:340px;background:linear-gradient(180deg,var(--band-top),var(--band-bottom));color:var(--white)}
.features .wrap{display:flex;justify-content:space-between;padding-top:60px}
.feature{width:280px;text-align:center}
.feature svg{height:60px}
.feature h3{margin-top:22px;font-size:17px;font-weight:700;letter-spacing:.5px}
.feature p{margin-top:10px;font-size:12px;line-height:19px;color:#e4ecf2}

/* newsletter */
.newsletter{height:80px;background:var(--dark)}
.newsletter .wrap{display:flex;align-items:center;justify-content:center;height:80px;gap:18px}
.newsletter label{color:var(--white);font-size:13px;font-weight:600}
.newsletter .field{width:310px;height:30px;background:var(--white);font-size:11px;color:#999;line-height:30px;padding-left:12px}
.newsletter .btn-submit{height:30px;padding:0 36px;background:var(--accent);color:var(--white);font-size:12px;font-weight:700;line-height:30px}

/* highlight boxes */
.highlights{height:440px;background:var(--light)}
.highlights .wrap{display:flex;justify-content:space-between;padding-top:60px}
.box{width:300px;height:340px;background:var(--white);padding:22px 22px;box-shadow:0 1px 3px rgba(0,0,0,.08);position:relative}
.box h2{font-size:17px;font-weight:700;padding-bottom:12px;border-bottom:1px solid #e2e2e2}
.news-item{display:flex;gap:14px;margin-top:20px}
.thumb{width:80px;height:64px;flex:none;background:linear-gradient(135deg,#c9b8a6,#6e7c8a)}
.thumb.house{background:linear-gradient(135deg,#e3c9a8,#9aa9b5)}
.news-item .date{font-size:11px;color:var(--date)}
.news-item .title{font-size:12px;font-weight:700;margin-top:2px}
.news-item .desc{font-size:11px;color:var(--muted);line-height:16px}
.btn-read{position:absolute;left:22px;bottom:24px;background:var(--accent);color:var(--white);font-size:10px;font-weight:700;padding:7px 12px}
.video{margin-top:18px;width:256px;height:230px;position:relative;background:linear-gradient(160deg,#f2f2f2,#c7ccd1 60%,#8e979f)}
.video-play{position:absolute;left:98px;top:72px}
.video-bar{position:absolute;left:0;right:0;bottom:0;height:40px;background:rgba(30,30,30,.85);color:var(--white);font-size:11px;display:flex;align-items:center;gap:14px;padding-left:10px}

/* investor news */
.investor-news{height:260px}
.investor-news .wrap{display:flex;padding-top:40px}
.investor-intro{width:220px;margin-left:-20px}
.investor-intro h2{font-size:18px;font-weight:700}
.investor-intro p{margin-top:26px;font-size:11px;line-height:17px;color:var(--muted)}
.gallery{display:flex;gap:20px;margin-left:40px;margin-top:24px}
.gallery figure{width:220px}
.gallery .photo{height:120px;background:linear-gradient(160deg,#8fa9c2,#d7d0c3 55%,#6a6d66)}
.gallery .photo.dusk{background:linear-gradient(160deg,#3c4f66,#a68e6a 60%,#2f3338)}
.gallery .photo.day{background:linear-gradient(160deg,#bcd2e6,#f0ece4 55%,#7e8779)}
.gallery figcaption{margin-top:10px;font-size:12px;font-style:italic;color:var(--link)}
.gallery small{display:block;font-size:11px;font-style:italic;color:var(--muted)}

/* contact map */
.contact{height:440px;position:relative}
.map{position:absolute;inset:0;background:linear-gradient(135deg,#e6e6e4,#d3d4d2 50%,#e2e2df)}
.contact-card{position:absolute;left:320px;top:80px;width:520px;height:280px;display:flex;box-shadow:0 2px 8px rgba(0,0,0,.2)}
.card-brand{width:220px;background:var(--white);display:flex;flex-direction:column;align-items:center;justify-content:center;gap:14px}
.card-brand .brand-line{display:flex;align-items:center;gap:8px}
.card-brand .brand-square{width:22px;height:22px}
.card-brand .brand-name{font-size:17px}
.card-brand p{font-size:11px;color:var(--link);text-align:center;width:140px;line-height:16px}
.card-info{flex:1;background:#4c6377;color:var(--white);padding:70px 0 0 26px;font-size:12px}
.card-info li{list-style:none;display:flex;align-items:center;gap:12px;margin-bottom:22px}

/* footer */
.site-footer{height:52px;background:var(--dark);color:#cfcfcf;font-size:11px}
.site-footer .wrap{display:flex;align-items:center;justify-content:space-between;height:52px}
.social{display:flex;gap:8px}
.social span{width:22px;height:22px;border-radius:50%;background:#8a8a8a}
</style>
</head>
<body>

<header class="site-header">
  <div class="brand">
    <span class="brand-square"></span>
    <span class="brand-name">Veluna Real Estate</span>
  </div>
  <div class="header-actions">
    <div class="btn-profile">
      <svg width="18" height="20" viewBox="0 0 18 20"><rect x="1" y="1" width="16" height="18" fill="#d9362b"/><rect x="4" y="6" width="10" height="2" fill="#fff"/><rect x="4" y="11" width="10" height="2" fill="#fff"/></svg>
      COMPANY PROFILE
    </div>
    <div class="btn-login">CUSTOMER LOGIN</div>
  </div>
</header>

<nav class="main-nav">
  <ul>
    <li class="active">HOME</li>
    <li>ABOUT US</li>
    <li>PROPERTIES</li>
    <li>SERVICES &amp; NEWS</li>
    <li>REFERENCES</li>
    <li>CONTACT US</li>
  </ul>
</nav>

<section class="hero">
  <div class="hero-photo" role="img" aria-label="Sea view with sky over calm water"></div>
  <div class="hero-building" role="img" aria-label="Modern glass-fronted residential building with balconies"></div>
  <div class="hero-copy">
    <h1 class="hero-title">REAL ESTATE DEVELOPMENT<br>&amp; BROKERAGE COMPANY IN AUSTRIA</h1>
    <p class="hero-text">Neque porro quisquam est qui dolorem ipsum quia dolor sit amet, consectetur, adipisci velit. Neque porro quisquam est qui dolorem ipsum quia dolor sit amet.</p>
    <span class="btn-more">View More</span>
  </div>
  <div class="hero-dots"><span class="on"></span><span></span><span></span><span></span></div>
</section>

<section class="features">
  <div class="wrap">
    <div class="feature">
      <svg viewBox="0 0 60 60" width="60"><path d="M8 28h10v26H8z M22 28l10-20c5 0 7 4 6 9l-2 9h14c4 0 6 4 5 7l-5 17c-1 3-3 4-6 4H22z" fill="#fff"/></svg>
      <h3>NEQUE PORRO</h3>
      <p>Lorem ipsum dolor sit amet, consectetur adipiscing elit, sed do eiusmod tempor incididunt ut labore et dolore magna.</p>
    </div>
    <div class="feature">
      <svg viewBox="0 0 60 60" width="60"><path d="M30 6 4 30h8v24h14V40h8v14h14V30h8z" fill="#fff"/></svg>
      <h3>QUISQUAM EST</h3>
      <p>Lorem ipsum dolor sit amet, consectetur adipiscing elit, sed do eiusmod tempor incididunt ut labore et dolore magna.</p>
    </div>
    <div class="feature">
      <svg viewBox="0 0 60 60" width="60"><g fill="#fff"><circle cx="30" cy="30" r="17"/><rect x="25" y="4" width="10" height="12"/><rect x="25" y="44" width="10" height="12"/><rect x="4" y="25" width="12" height="10"/><rect x="44" y="25" width="12" height="10"/><rect x="25" y="4" width="10" height="12" transform="rotate(45 30 30)"/><rect x="25" y="44" width="10" height="12" transform="rotate(45 30 30)"/><rect x="4" y="25" width="12" height="10" transform="rotate(45 30 30)"/><rect x="44" y="25" width="12" height="10" transform="rotate(45 30 30)"/></g><circle cx="30" cy="30" r="7" fill="#5a7b95"/></svg>
      <h3>DOLOR SIT AMET</h3>
      <p>Lorem ipsum dolor sit amet, consectetur adipiscing elit, sed do eiusmod tempor incididunt ut labore et dolore magna.</p>
    </div>
  </div>
</section>

<section class="newsletter">
  <div class="wrap">
    <label>Subscribe to our Newsletter to be invited</label>
    <div class="field">Enter your email ID</div>
    <div class="btn-submit">SUBMIT</div>
  </div>
</section>

<section class="highlights">
  <div class="wrap">
    <article class="box">
      <h2>INVESTORS NEWS</h2>
      <div class="news-item">
        <div class="thumb" role="img" aria-label="Business meeting photo"></div>
        <div><div class="date">12 March 2015</div><div class="title">Lorem ipsum dolor</div><div class="desc">sit amet, consectetur adipiscing elit magna.</div></div>
      </div>
      <div class="news-item">
        <div class="thumb" role="img" aria-label="Investors at work photo"></div>
        <div><div class="date">12 March 2015</div><div class="title">Lorem ipsum dolor</div><div class="desc">sit amet, consectetur adipiscing elit magna.</div></div>
      </div>
      <span class="btn-read">READ ALL</span>
    </article>
    <article class="box">
      <h2>VIDEO</h2>
      <div class="video" role="img" aria-label="Video still of a bright modern interior">
        <svg class="video-play" width="60" height="60" viewBox="0 0 60 60"><circle cx="30" cy="30" r="28" fill="rgba(0,0,0,.55)"/><path d="M24 18l18 12-18 12z" fill="#fff"/></svg>
        <div class="video-bar">
          <svg width="16" height="16" viewBox="0 0 16 16"><circle cx="8" cy="8" r="7" fill="none" stroke="#fff" stroke-width="1.5"/><path d="M6 4.5l5 3.5-5 3.5z" fill="#fff"/></svg>
          Elesent Ipsum Quia
        </div>
      </div>
    </article>
    <article class="box">
      <h2>FAMILY BUSINESS NEWS</h2>
      <div class="news-item">
        <div class="thumb house" role="img" aria-label="Family home exterior photo"></div>
        <div><div class="date">12 March 2015</div><div class="title">Lorem ipsum dolor</div><div class="desc">sit amet, consectetur adipiscing elit magna.</div></div>
      </div>
      <div class="news-item">
        <div class="thumb house" role="img" aria-label="Residential property photo"></div>
        <div><div class="date">12 March 2015</div><div class="title">Lorem ipsum dolor</div><div class="desc">sit amet, consectetur adipiscing elit magna.</div></div>
      </div>
      <span class="btn-read">READ ALL</span>
    </article>
  </div>
</section>

<section class="investor-news">
  <div class="wrap">
    <div class="investor-intro">
      <h2>INVESTOR NEWS</h2>
      <p>Neque porro quisquam est qui dolorem ipsum quia dolor sit amet, consectetur, adipisci velit. Neque porro quisquam est.</p>
    </div>
    <div class="gallery">
      <figure>
        <div class="photo" role="img" aria-label="Luxury villa exterior with lawn"></div>
        <figcaption>Exceptional sit cause dolor<small>posted on 25 March 2015</small></figcaption>
      </figure>
      <figure>
        <div class="photo dusk" role="img" aria-label="Modern house lit at dusk"></div>
        <figcaption>Exceptional sit cause dolor<small>posted on 25 March 2015</small></figcaption>
      </figure>
      <figure>
        <div class="photo day" role="img" aria-label="White contemporary residence by day"></div>
        <figcaption>Exceptional sit cause dolor<small>posted on 25 March 2015</small></figcaption>
      </figure>
    </div>
  </div>
</section>

<section class="contact">
  <div class="map" role="img" aria-label="City street map showing the office location"></div>
  <div class="contact-card">
    <div class="card-brand">
      <div class="brand-line"><span class="brand-square"></span><span class="brand-name">Veluna Real Estate</span></div>
      <p>We look forward to your enquiry.</p>
    </div>
    <ul class="card-info">
      <li><svg width="14" height="18" viewBox="0 0 14 18"><path d="M7 0a7 7 0 0 0-7 7c0 5 7 11 7 11s7-6 7-11a7 7 0 0 0-7-7zm0 10a3 3 0 1 1 0-6 3 3 0 0 1 0 6z" fill="#fff"/></svg>Locations: Vienna, Dubai and Abu Dhabi</li>
      <li><svg width="16" height="16" viewBox="0 0 16 16"><path d="M3 1l3 3-2 2c1 2 4 5 6 6l2-2 3 3-2 2C7 15 1 9 1 3z" fill="#fff"/></svg>Call Us: +000 555 0142</li>
      <li><svg width="16" height="12" viewBox="0 0 16 12"><rect x="0.5" y="0.5" width="15" height="11" fill="none" stroke="#fff"/><path d="M1 1l7 6 7-6" fill="none" stroke="#fff"/></svg>Email: info@veluna.example</li>
    </ul>
  </div>
</section>

<footer class="site-footer">
  <div class="wrap">
    <span>Copyright © Veluna 2014 - All Rights Reserved.</span>
    <div class="social"><span></span><span></span><span></span><span></span><span></span></div>
  </div>
</footer>

</body>
</html>
```